Tanwick Services Website Design

We have most content but require a professional design. We have a logo already and will need it utilized along with several of the photos from the attached documentation.
First page should have our mission and Vision and the synapsis provided in the word document. Visitors will be prompted to select from one of our 3 divisions from this page.
Each division will have the same list of tabs : About, Services, Safety, Careers and Contact.
Photos on each divisions page should be representative of the divisions offerings. The word doc attached contains the requested content and we are open to edits that would complement and fill the website.
I like the Morvalix site www.morvalix-demo.net - they are our competition so cant be modeled directly after this.
Please include prompts to request quote at each service page. align the format of the geotechnical page to the other 2 divisions.
I used chat gpt for some of the content so will need it optimized for SCO.

```html
<!DOCTYPE html>
<html lang="en">
<head>
<meta charset="utf-8">
<title>Tanwick Services</title>
<link href="https://fonts.googleapis.com/css2?family=Lato:wght@400;700;900&family=Oswald:wght@500;600&display=swap" rel="stylesheet">
<style>
:root{
  --red:#ee1c25;
  --ink:#111111;
  --text:#333333;
  --muted:#555555;
  --grey:#f5f5f5;
  --footer:#f3f3f3;
  --bar:#1b1b1b;
  --white:#ffffff;
}
*{margin:0;padding:0;box-sizing:border-box}
html,body{width:1200px;height:2627px;overflow:hidden}
body{position:relative;font-family:'Lato',sans-serif;color:var(--text);background:var(--white)}
.abs{position:absolute}
.btn{position:absolute;background:var(--red);color:var(--white);font-size:13px;font-weight:700;display:flex;align-items:center;justify-content:center;text-decoration:none}
.brand{font-family:'Lato',sans-serif;font-weight:900;color:var(--red);letter-spacing:6px;line-height:1}

/* hero */
.hero{position:absolute;left:0;top:0;width:1200px;height:565px;background:linear-gradient(100deg,#dcebf5 0%,#bcd9ea 40%,#6fa9cf 75%,#3d7fae 100%)}
.hero-photo{position:absolute;left:560px;top:60px;width:640px;height:505px;background:radial-gradient(ellipse at 70% 55%,rgba(230,140,60,.45),rgba(60,120,170,0) 60%)}
.nav a{position:absolute;top:34px;font-size:13px;color:var(--ink);text-decoration:none}
.hero h1{position:absolute;left:142px;top:174px;font-family:'Oswald',sans-serif;font-weight:600;font-size:46px;line-height:53px;color:var(--ink)}
.hero .sub{position:absolute;left:142px;top:340px;font-size:20px;font-weight:700;line-height:26px;color:var(--ink)}

/* services */
.section-title{position:absolute;width:1200px;text-align:center;color:var(--red);font-size:32px;font-weight:700}
.services-sub{position:absolute;top:664px;width:1200px;text-align:center;font-size:13px;font-weight:700;color:var(--text)}
.service{position:absolute;top:700px;width:240px;height:142px;text-align:center}
.service svg{display:block;margin:10px auto 0}
.service h3{font-size:14.5px;font-weight:700;color:var(--ink);margin-top:10px}
.service p{font-size:11px;line-height:18px;color:var(--muted);margin-top:4px}
.divider{position:absolute;top:700px;width:1px;height:142px;background:#e5e5e5}

/* vision */
.vision-photo{position:absolute;left:0;top:983px;width:564px;height:437px;background:linear-gradient(160deg,#3e5a3a 0%,#6d7d66 45%,#a9a59a 75%,#c9c3b6 100%)}
.vision-text{position:absolute;left:564px;top:983px;width:636px;height:437px;background:var(--grey)}
.vision-text h2{position:absolute;left:58px;font-size:22px;font-weight:700;color:var(--red)}
.vision-text p{position:absolute;left:58px;width:438px;font-size:12.5px;line-height:21.7px;color:var(--ink)}

/* divisions */
.divisions-band{position:absolute;left:0;top:1505px;width:1200px;height:353px;background:linear-gradient(180deg,#2c3a33 0%,#4a5a52 50%,#5a655e 100%)}
.divisions-band h2{position:absolute;top:80px;width:1200px;text-align:center;color:var(--white);font-size:32px;font-weight:700}
.divisions-panel{position:absolute;left:141px;top:1644px;width:918px;height:426px;background:var(--white)}
.division{position:absolute;top:1681px;width:275px}
.division .photo{width:275px;height:211px}
.division h3{margin:26px 0 0 6px;font-size:17px;font-weight:700;color:var(--red)}
.division p{margin:6px 0 0 6px;font-size:11px;line-height:19px;color:var(--ink);width:268px}
.division .more{display:flex;align-items:center;gap:6px;margin:6px 0 0 6px;font-size:13px;font-weight:700;color:var(--red)}

/* cta */
.footer-bg{position:absolute;left:0;top:2269px;width:1200px;height:303px;background:var(--footer)}
.cta{position:absolute;left:184px;top:2113px;width:833px;height:223px;background:var(--white);box-shadow:0 8px 0 -2px #d6d6d6}
.cta h2{position:absolute;top:36px;width:833px;text-align:center;font-size:23px;line-height:30.5px;font-weight:700;color:var(--ink)}
.cta h2 span{color:var(--red)}

/* footer */
.footer h4{position:absolute;font-size:18px;font-weight:700;color:var(--ink)}
.rule{position:absolute;height:1px;background:#cfcfcf}
.rule::before{content:"";position:absolute;left:0;top:-1px;width:40px;height:3px;background:var(--red)}
.qlink{position:absolute;font-size:13px;color:var(--ink);display:flex;align-items:center;gap:9px}
.qlink::before{content:"»";color:var(--red);font-size:11px}
.contact-item{position:absolute;font-size:13px;color:var(--ink);line-height:20px}
.contact-item b{display:block}
.bottom-bar{position:absolute;left:0;top:2572px;width:1200px;height:55px;background:var(--bar)}
.bottom-bar .copy{position:absolute;left:145px;top:19px;font-size:12.5px;color:var(--white)}
.social{position:absolute;top:14px;width:28px;height:28px;border-radius:50%;background:var(--red)}
</style>
</head>
<body>

<section class="hero">
  <div class="hero-photo" role="img" aria-label="Photo of two site engineers in hard hats reviewing plans, with glowing industry icons over a blue sky"></div>
  <div class="brand abs" style="left:142px;top:22px;font-size:42px">TANWICK</div>
  <nav class="nav">
    <a style="left:653px">Home</a>
    <a style="left:721px">About Us</a>
    <a style="left:808px">Safety</a>
    <a style="left:877px">Careers</a>
  </nav>
  <a class="btn" style="left:954px;top:25px;width:105px;height:34px">Contact Us</a>
  <h1>Delivering Safe,<br>Reliable Aerial Access<br>&amp; Maintenance Services</h1>
  <p class="sub">To Oil &amp; Gas,Construction, Utility, &amp;<br>Renewable Energy Sector</p>
  <a class="btn" style="left:142px;top:409px;width:105px;height:35px">Contact Us</a>
</section>

<h2 class="section-title" style="top:618px">Tanwick Services</h2>
<p class="services-sub">Delivering Safe Reliable Aerial Access And Maintenance Services</p>

<div class="service" style="left:120px">
  <svg width="50" height="52" viewBox="0 0 50 52" fill="none" stroke="#ee1c25" stroke-width="2"><path d="M3 50h44M6 50V24h12v26M18 50V14h10v36M28 50V30h16v20M10 24V8h4v16M22 14V4h4v10"/><path d="M32 36h8M32 42h8M9 30h6M9 38h6"/></svg>
  <h3>Oil &amp; Gas</h3>
  <p>Lorem ipsum dolor sit amet, consectetur<br>adipiscing egestas metus auctor elit.</p>
</div>
<div class="divider" style="left:360px"></div>
<div class="service" style="left:360px">
  <svg width="54" height="56" viewBox="0 0 54 56" fill="none" stroke="#ee1c25" stroke-width="2"><path d="M4 54h46M14 54l8-40h8l8 40M18 34h18M16 44h22M8 10h36l4 6H8zM44 16v10"/><rect x="42" y="26" width="6" height="8"/></svg>
  <h3>Construction</h3>
  <p>Lorem ipsum dolor sit amet, consectetur<br>adipiscing egestas metus auctor elit.</p>
</div>
<div class="divider" style="left:600px"></div>
<div class="service" style="left:600px">
  <svg width="50" height="50" viewBox="0 0 50 50" fill="none" stroke="#ee1c25" stroke-width="2"><circle cx="25" cy="25" r="15"/><circle cx="25" cy="25" r="7"/><path d="M25 2v8M25 40v8M2 25h8M40 25h8M9 9l6 6M35 35l6 6M9 41l6-6M35 15l6-6"/></svg>
  <h3>Utility</h3>
  <p>Lorem ipsum dolor sit amet, consectetur<br>adipiscing egestas metus auctor elit.</p>
</div>
<div class="divider" style="left:838px"></div>
<div class="service" style="left:840px">
  <svg width="50" height="50" viewBox="0 0 50 50" fill="none" stroke="#ee1c25" stroke-width="2"><path d="M8 18a19 19 0 0 1 34-4M42 32a19 19 0 0 1-34 4"/><path d="M42 6v8h-8M8 44v-8h8"/><path d="M25 36V22c0-5 4-8 8-8 0 6-3 10-8 10"/></svg>
  <h3>Renewable Energy Industries</h3>
  <p>Lorem ipsum dolor sit amet, consectetur<br>adipiscing egestas metus auctor elit.</p>
</div>
<a class="btn" style="left:548px;top:863px;width:105px;height:35px">Contact Us</a>

<div class="vision-photo" role="img" aria-label="Photo of a white aerial lift truck parked on a gravel lot beside forest"></div>
<section class="vision-text">
  <h2 style="top:42px">Our Vision</h2>
  <p style="top:74px">To be the leading provider of aerial access, geotechnical drilling, and service solutions, setting the standard for excellence in safety, efficiency, and environmental stewardship.</p>
  <h2 style="top:155px">Our Mission</h2>
  <p style="top:187px">At Tanwick, our mission is to deliver unparalleled aerial access, geotechnical drilling, and service and maintenance solutions, consistently exceeding our clients' expectations. We strive to achieve this by investing in cutting-edge technology, fostering a culture of safety and continuous improvement, and prioritizing environmental sustainability. Through collaboration, integrity, and dedication, we aim to contribute to the success of our clients while maintaining the highest standards of quality and professionalism.</p>
  <a class="btn" style="left:58px;top:355px;width:106px;height:35px">Contact Us</a>
</section>

<section class="divisions-band" role="img" aria-label="Aerial photo of a worker in a lift basket above a rural town">
  <h2>Our Divisions</h2>
</section>
<div class="divisions-panel"></div>

<article class="division" style="left:175px">
  <div class="photo" role="img" aria-label="Photo of a lift boom reaching a tall white tower under a blue sky" style="background:linear-gradient(180deg,#3f86d6 0%,#8dbbe8 60%,#8f8a5e 100%)"></div>
  <h3>Aerial Access</h3>
  <p>Tanwick is a full-service wind energy service provider specializing in blade access &amp; repair, service and maintenance, and trouble shooting on most wind turbine platforms.</p>
  <div class="more">Read More <svg width="16" height="8" viewBox="0 0 16 8" fill="none" stroke="#ee1c25" stroke-width="1.5"><path d="M0 4h15M11 1l4 3-4 3"/></svg></div>
</article>
<article class="division" style="left:462px">
  <div class="photo" role="img" aria-label="Photo of a red tracked geotechnical drill rig on green grass" style="background:linear-gradient(180deg,#1f3a22 0%,#2f5a2c 50%,#4d7a34 100%)"></div>
  <h3>Geotechnical Drilling</h3>
  <p>Lorem ipsum dolor sit amet onsctetur adipiscing elit. Nullam porta turpis dui, ut ultricies nisi soicitudin et. Quisque tellus vitae mauris veenatis blandit. Nunc accumsan nisi ut pellentesque placerat.</p>
  <div class="more">Read More <svg width="16" height="8" viewBox="0 0 16 8" fill="none" stroke="#ee1c25" stroke-width="1.5"><path d="M0 4h15M11 1l4 3-4 3"/></svg></div>
</article>
<article class="division" style="left:750px">
  <div class="photo" role="img" aria-label="Photo of a white lift boom beside a wind turbine against a blue sky" style="background:linear-gradient(180deg,#2a6fc4 0%,#3f86d8 60%,#5a9ae0 100%)"></div>
  <h3>Renewable Energy Services</h3>
  <p>Lorem ipsum dolor sit amet onsctetur adipiscing elit. Nullam porta turpis dui, ut ultricies nisi soicitudin et. Quisque tellus vitae mauris veenatis blandit. Nunc accumsan nisi ut pellentesque placerat.</p>
  <div class="more">Read More <svg width="16" height="8" viewBox="0 0 16 8" fill="none" stroke="#ee1c25" stroke-width="1.5"><path d="M0 4h15M11 1l4 3-4 3"/></svg></div>
</article>

<div class="footer-bg"></div>
<section class="cta">
  <h2><span>TANWICK</span> is a Full Service Wind Energy Service Provider<br>Specializing In Blade Access And Repair, Service And Maintenance,<br>And Trouble Shooting On Most Wind Turbine Platforms.</h2>
  <a class="btn" style="left:391px;top:147px;width:106px;height:35px">Contact Us</a>
</section>

<footer class="footer">
  <h4 style="left:143px;top:2386px">Quick Links</h4>
  <div class="rule" style="left:143px;top:2418px;width:110px"></div>
  <div class="qlink" style="left:145px;top:2437px">Home</div>
  <div class="qlink" style="left:145px;top:2466px">About</div>
  <div class="qlink" style="left:145px;top:2494px">Services</div>
  <div class="qlink" style="left:272px;top:2437px">Safety</div>
  <div class="qlink" style="left:272px;top:2466px">Careers</div>
  <div class="qlink" style="left:272px;top:2494px">Contact Us</div>

  <h4 style="left:506px;top:2386px">Contact Details</h4>
  <div class="rule" style="left:506px;top:2418px;width:141px"></div>
  <svg class="abs" style="left:506px;top:2441px" width="13" height="13" viewBox="0 0 24 24" fill="#ee1c25"><path d="M6.6 10.8a15 15 0 0 0 6.6 6.6l2.2-2.2a1 1 0 0 1 1-.25 11.4 11.4 0 0 0 3.6.57 1 1 0 0 1 1 1V20a1 1 0 0 1-1 1A17 17 0 0 1 3 4a1 1 0 0 1 1-1h3.5a1 1 0 0 1 1 1c0 1.25.2 2.450.57 3.570a1 1 0 0 1-.25 1z"/></svg>
  <div class="contact-item" style="left:527px;top:2439px"><b>Phone</b>(555)-014-2287</div>
  <svg class="abs" style="left:506px;top:2494px" width="14" height="11" viewBox="0 0 14 11" fill="#ee1c25"><rect width="14" height="11" rx="1"/><path d="M1 1l6 5 6-5" stroke="#fff" stroke-width="1.3" fill="none"/></svg>
  <div class="contact-item" style="left:527px;top:2490px"><b>Email</b>career@tanwickservices.com</div>

  <div class="brand abs" style="left:827px;top:2388px;font-size:27px;letter-spacing:4px">TANWICK</div>
  <svg class="abs" style="left:826px;top:2434px" width="11" height="16" viewBox="0 0 11 16" fill="#ee1c25"><path d="M5.5 0A5.5 5.5 0 0 0 0 5.5C0 10 5.5 16 5.5 16S11 10 11 5.5A5.5 5.5 0 0 0 5.5 0zm0 7.8a2.3 2.3 0 1 1 0-4.6 2.3 2.3 0 0 1 0 4.6z"/></svg>
  <div class="contact-item" style="left:847px;top:2429px">218 Ridge Road Elm Falls<br>AB T0M-4B1</div>
</footer>

<div class="bottom-bar">
  <p class="copy">© 2024 TANWICK. All Rights Reserved.</p>
  <span class="social" style="left:925px"></span>
  <span class="social" style="left:961px"></span>
  <span class="social" style="left:996px"></span>
  <span class="social" style="left:1031px"></span>
</div>

</body>
</html>
```